The hardcover "Velvet Register" (large size, Quarto 4º, 12 × 9 1/2 in, 30.5 × 24.15 cm) in German language as follows:

SAMTENES REGISTER (title)
der angesehensten Gründer und Führungskräfte Mitteldeutschlands 2014 (subtitle 1)
SACHSEN UND THÜRINGEN (subtitle 2, smaller than subtitle 1)

Korvalix (logo, WMF file attached)

Reason: The solutions are rather too childish and pre-made styles... is there anyone who can make it better? - a professional-looking business book (encyclopedia style, should have no color-pictures, no author's name, logo smaller due to the large size book)

Target Market(s)

business community

Requirements
Must have
• encyclopedia style large size book
must look professional and expensive

Nice to have
• - gold-color hardcover, or some gold-color elements
- some simple and decent graphic element (e.g. an ancient column, or some other architectural detail), if any
Should not have
• no color-pictures
no author's name

```html
<!DOCTYPE html>
<html lang="de">
<head>
<meta charset="utf-8">
<title>Samtenes Register – Sachsen und Thüringen 2014</title>
<link rel="stylesheet" href="https://fonts.googleapis.com/css2?family=Quicksand:wght@500;700&display=swap">
<style>
  :root {
    --cover-brown: #271710;
    --rule-bronze: #8a6536;
    --band-olive: #766223;
    --title-gold: #e6c21c;
    --subtitle-gold: #cfa928;
    --mark-bronze: #7e5c33;
    --strip-light: #33210f;
    --strip-dark: #1e120b;
  }
  * { margin: 0; padding: 0; box-sizing: border-box; }
  html, body {
    width: 950px;
    height: 1200px;
    overflow: hidden;
    background: var(--cover-brown);
  }
  .cover {
    position: relative;
    width: 950px;
    height: 1200px;
    background: var(--cover-brown);
    font-family: "Quicksand", sans-serif;
  }
  .rule {
    position: absolute;
    top: 0;
    width: 4px;
    height: 1200px;
    background: var(--rule-bronze);
  }
  .rule--left { left: 115px; }
  .rule--right { left: 350px; }
  .architecture-strip {
    position: absolute;
    left: 119px;
    top: 0;
    width: 231px;
    height: 1200px;
    background: linear-gradient(170deg, var(--strip-light) 0%, #2b1a10 50%, var(--strip-dark) 100%);
  }
  .accent-band {
    position: absolute;
    left: 814px;
    width: 91px;
    background: var(--band-olive);
  }
  .accent-band--upper { top: 0; height: 1063px; }
  .accent-band--lower { top: 1150px; height: 50px; }
  .publisher-mark {
    position: absolute;
    left: 90px;
    top: 165px;
    transform-origin: 0 0;
    transform: rotate(-90deg);
    display: flex;
    align-items: center;
    gap: 6px;
    color: var(--mark-bronze);
    font-weight: 700;
    font-size: 15px;
    line-height: 1;
    white-space: nowrap;
  }
  .publisher-mark__dot {
    width: 9px;
    height: 9px;
    border-radius: 50%;
    background: var(--mark-bronze);
  }
  .title-block {
    position: absolute;
    left: 0;
    top: 0;
  }
  .title-block text { font-family: "Quicksand", sans-serif; }
  .title { fill: var(--title-gold); font-weight: 700; }
  .subtitle { fill: var(--subtitle-gold); font-weight: 500; }
  .region { fill: var(--subtitle-gold); font-weight: 700; letter-spacing: 0.06em; }
</style>
</head>
<body>
<main class="cover">
  <div class="architecture-strip" role="img" aria-label="Dunkel getöntes Foto eines klassizistischen Portals mit korinthischer Säule und Statue"></div>
  <div class="rule rule--left"></div>
  <div class="rule rule--right"></div>

  <div class="publisher-mark">
    <span class="publisher-mark__name">Korvalix</span>
    <span class="publisher-mark__dot"></span>
  </div>

  <div class="accent-band accent-band--upper"></div>
  <div class="accent-band accent-band--lower"></div>

  <svg class="title-block" width="950" height="1200" viewBox="0 0 950 1200">
    <text class="title" x="358" y="1117" font-size="50" textLength="545" lengthAdjust="spacingAndGlyphs">SAMTENES REGISTER</text>
    <text class="subtitle" x="366" y="1133" font-size="15" textLength="537" lengthAdjust="spacingAndGlyphs">der angesehensten Gründer und Führungskräfte Mitteldeutschlands 2014</text>
    <text class="region" x="363" y="1149" font-size="9">SACHSEN UND THÜRINGEN</text>
  </svg>
</main>
</body>
</html>
```